Business Card for Marco Thieblin Analytics and Marco Thieblin Photography

I want a double sided business card: on one side it should be about "Marco Thieblin Photography" and on the other side about "Marco Thieblin Analytics". You find the logos for these two projects in the attachments. The design of the business card should blend well with the colours and fonts used in the logos and should be quite simple, yet look professional and modern.

In addition to my name, there should be content for a telephone number, e-mail address and website. There should be little icons (for telephone, email and web) before these fields. I do not want a postal mail address field.
Lastly you should indicate that people can contact me in the following languages: Lëtzebuergesch, Deutsch, Français, English, Castellano, Ido
This should be very unobtrusive: either in a small muted font or with little icons (preferably without using flags as flags represent nations, not languages - one possibility would be by using the 2 letter ISO codes).

The design should be delivered in Adobe Illustrator format or something similar that I can edit easily, as it's possible that I will change my e-mail address and domain soon.

I hope this was detailed enough but still leaves you some freedom for designing something nice.

Thank you!
Marco

Industry/Entity Type

Business

Contact Information for Business Card

e-mail address: mtb_@orvenmail.example
website: www.marcothieblin.example (for Marco Thieblin Photography)
website: kelvodata.example/mtb (for Marco Thieblin Analytics - this address is likely to change)
phone: +352 691 987 654 (not my real number - I prefer not to publish it on the web)

Requirements
Nice to have
• A speech bubble followed by the 2-letter language codes (lb, de, fr, en, es, io) or even speech bubble icons for every language would be nice and eliminates the need to put text like 'you can contact me in the following languages'.

```html
<!DOCTYPE html>
<html lang="en">
<head>
<meta charset="utf-8">
<title>Marco Thieblin Photography – Business Card</title>
<link href="https://fonts.googleapis.com/css2?family=Open+Sans:wght@400;700&display=swap" rel="stylesheet">
<style>
  :root {
    --page-bg: #ffffff;
    --card-bg: #231f20;
    --card-shadow: #555555;
    --text-light: #ffffff;
    --icon-blue: #1aa3dd;
    --brand-orange: #f08a24;
    --bubble-green-dark: #0b6b3a;
    --bubble-green-light: #7cc242;
    --bubble-shadow: #6d6e70;
  }
  * { margin: 0; padding: 0; box-sizing: border-box; }
  html, body {
    width: 1200px;
    height: 1000px;
    overflow: hidden;
    background: var(--page-bg);
    font-family: "Open Sans", sans-serif;
  }
  .business-card {
    position: absolute;
    left: 206px;
    top: 275px;
    width: 788px;
    height: 450px;
    background: var(--card-bg);
    box-shadow: 7px 6px 6px var(--card-shadow);
  }
  .brand-name {
    position: absolute;
    left: 0;
    width: 100%;
    top: 138px;
    text-align: center;
    color: var(--brand-orange);
    font-weight: 700;
    font-size: 34px;
    letter-spacing: 0.5px;
  }
  .contact-list {
    position: absolute;
    left: 52px;
    top: 290px;
    list-style: none;
  }
  .contact-item {
    display: flex;
    align-items: center;
    height: 34px;
    color: var(--text-light);
    font-weight: 700;
    font-size: 16px;
  }
  .contact-item + .contact-item { margin-top: 0; }
  .contact-phone { margin-top: 0; }
  .contact-email { margin-top: 24px; }
  .contact-web { margin-top: 16px; }
  .contact-icon {
    width: 34px;
    height: 34px;
    margin-right: 11px;
    flex: none;
  }
  .language-bubble {
    position: absolute;
    left: 552px;
    top: 362px;
    width: 196px;
    height: 80px;
  }
  .language-codes {
    position: absolute;
    left: 566px;
    top: 380px;
    width: 168px;
    display: flex;
    justify-content: space-between;
    color: var(--text-light);
    font-size: 17px;
    line-height: 24px;
  }
</style>
</head>
<body>
  <div class="business-card">
    <div class="brand-name">Marco Thieblin Photography</div>

    <ul class="contact-list">
      <li class="contact-item contact-phone">
        <svg class="contact-icon" viewBox="0 0 34 34" fill="none" stroke="var(--icon-blue)" stroke-width="2" stroke-linecap="round" stroke-linejoin="round">
          <path d="M8 7 L12 6 L15 12 L12 14 C13 18 16 21 20 22 L22 19 L28 22 L27 26 C25 29 21 29 16 26 C11 23 7 18 6 13 C5 10 6 8 8 7 Z"/>
          <path d="M19 5 C24 5 28 9 28 14"/>
          <path d="M19 9 C22 9 24 11 24 14"/>
        </svg>
        <span>+352 691 987 654</span>
      </li>
      <li class="contact-item contact-email">
        <svg class="contact-icon" viewBox="0 0 34 34" fill="none" stroke="var(--icon-blue)" stroke-width="2" stroke-linejoin="round">
          <rect x="4" y="9" width="26" height="17" rx="1"/>
          <path d="M4 9 L17 19 L30 9"/>
        </svg>
        <span>mtb_@orvenmail.example</span>
      </li>
      <li class="contact-item contact-web">
        <svg class="contact-icon" viewBox="0 0 34 34" fill="none" stroke="var(--icon-blue)" stroke-width="2.4">
          <circle cx="17" cy="17" r="15"/>
          <ellipse cx="17" cy="17" rx="6.5" ry="15"/>
          <line x1="2" y1="17" x2="32" y2="17"/>
          <path d="M5 9 H29 M5 25 H29"/>
        </svg>
        <span>www.marcothieblin.example</span>
      </li>
    </ul>

    <svg class="language-bubble" viewBox="0 0 196 80" aria-hidden="true">
      <defs>
        <linearGradient id="bubbleGreen" x1="0" y1="0" x2="1" y2="0">
          <stop offset="0" stop-color="var(--bubble-green-dark)"/>
          <stop offset="1" stop-color="var(--bubble-green-light)"/>
        </linearGradient>
      </defs>
      <path d="M8 5 H190 Q196 5 196 12 V52 Q196 58 190 58 H186 V63 L180 58 H8 Q4 58 4 52 V12 Q4 5 8 5 Z" fill="var(--bubble-shadow)"/>
      <path d="M6 0 H184 Q190 0 190 7 V50 Q190 55 184 55 H176 L182 78 L168 55 H6 Q0 55 0 49 V7 Q0 0 6 0 Z" fill="url(#bubbleGreen)"/>
      <rect x="7" y="7" width="176" height="41" rx="6" fill="var(--card-bg)"/>
    </svg>
    <div class="language-codes">
      <span>lb</span><span>de</span><span>fr</span><span>en</span><span>es</span><span>io</span>
    </div>
  </div>
</body>
</html>
```